Flyer Design Project

I provide workshops for teachers, students and parents on organization - specifically laying out 3 goals, their accompanying activities and actions in 3 three hour sessions.

Please go to my website to see my brain logo. I need a flyer with the information typed below. The information may be changed and/or added to in way you see fit to better communicate the organizational intent.This is not for speech therapy clients, rather, it is for any and everyone who needs help writing out goals.

I would like the design of the flyer to reflect the concept of organization in a unique way.

http://themindcraftstudyhouse.com/wp-content/uploads/2012/02/websitelogo2.jpg

ORGANIZATION

Write out your goals for the year.

How to organize your life in 3 easy steps.
Have fun organizing your life and plans.
Join a group of people dedicated to organizing all areas of life.
Complete your tasks in a fast, fun game format.
Walk away with your major goals broken down into their component parts and organize on a yearly calendar.
Three 3 hour days spent in making your life happier, less stressed and with realistic picture of what needs to be accomplished.
more effective in everything I do.
Being organized helps free our minds, enjoy relationships more, feel happier, and have greater meaning in life.

You will walk away with detailed plans for 2013.

COST: $600 for all three days.

WHO: Led by Maren Holtby, Cognitive Speech Therapist
WHERE: 4971 E Pruett Ave
Kennewick, WA 99336
509-218-3907

Requirements
Must have
• My logo from my website. A unique organized appearance.

```html
<!DOCTYPE html>
<html lang="en">
<head>
<meta charset="utf-8">
<title>Organize and Revitalize Your Life – Workshop Flyer</title>
<link href="https://fonts.googleapis.com/css2?family=Roboto+Condensed:wght@700&family=Tinos:wght@400;700&family=Arimo:ital,wght@0,400;0,700;1,400&family=Jost:wght@400;500&family=Cormorant+SC:wght@600&display=swap" rel="stylesheet">
<style>
  :root {
    --navy: #1a1a6e;
    --navy-deep: #12105a;
    --blue: #1f55a8;
    --cream: #fdf7d8;
    --cream-light: #fffdf0;
    --gold: #f2cf2a;
    --brick: #a8321c;
    --brick-light: #c4523a;
    --ink: #1e1e1e;
    --grey-shadow: rgba(0,0,0,.18);
    --white: #ffffff;
  }
  * { margin: 0; padding: 0; box-sizing: border-box; }
  html, body { width: 868px; height: 1200px; overflow: hidden; background: var(--white); }
  .flyer { position: relative; width: 868px; height: 1200px; overflow: hidden;
    background: linear-gradient(180deg, var(--cream-light) 0%, var(--white) 40%, var(--white) 78%, var(--cream) 100%); }
  .backdrop { position: absolute; inset: 0; }
  .headline { position: absolute; left: 43px; top: 38px; font: 700 36px/1 "Roboto Condensed", sans-serif; color: var(--navy); letter-spacing: -.2px; }
  .presenter { position: absolute; right: 26px; top: 38px; text-align: right; }
  .presenter-name { font: 400 29px/1 "Arimo", sans-serif; color: var(--gold); }
  .presenter-role { margin-top: 8px; font: italic 400 19px/1 "Arimo", sans-serif; color: var(--white); }
  .brain-art { position: absolute; left: 48px; top: 110px; width: 366px; height: 285px; border-radius: 48% 52% 46% 40%;
    background: radial-gradient(circle at 55% 45%, #d8342a 0%, #f08a1e 30%, #f4c21c 55%, #2a8fd0 85%, rgba(40,130,210,0) 100%); }
  .steps { position: absolute; right: 42px; top: 152px; text-align: right; font: 700 41px/1 "Tinos", serif; color: var(--white); letter-spacing: 1px; }
  .steps li { list-style: none; height: 66px; }
  .benefits { position: absolute; left: 27px; top: 438px; width: 426px; height: 467px; background: var(--white);
    border-radius: 10px; box-shadow: 0 0 9px var(--grey-shadow); padding: 18px 20px 0 15px; }
  .benefits li { list-style: none; position: relative; padding-left: 18px; margin-bottom: 19px;
    font: 400 15.5px/20px "Arimo", sans-serif; color: var(--ink); text-align: justify; }
  .benefits li::before { content: ""; position: absolute; left: 0; top: 5px; width: 10px; height: 10px; border-radius: 50%;
    background: radial-gradient(circle at 35% 35%, #f08070, #c8281c); }
  .benefits-pointer { position: absolute; left: 181px; top: 903px; width: 0; height: 0;
    border-left: 17px solid transparent; border-right: 17px solid transparent; border-top: 38px solid var(--white); }
  .takeaway { position: absolute; left: 27px; top: 922px; width: 426px; height: 115px; border-radius: 6px;
    background: linear-gradient(180deg, var(--brick-light), var(--brick)); color: var(--white); text-align: center;
    font: 600 31px/41px "Cormorant SC", serif; padding-top: 14px; letter-spacing: .5px; }
  .group-photo { position: absolute; left: 465px; top: 350px; width: 395px; height: 525px; border-radius: 40% 40% 30% 30%;
    background: radial-gradient(ellipse at 50% 45%, #c69a7e 0%, #d9cfc4 45%, #f3f1ee 75%, rgba(255,255,255,0) 100%); }
  .testimonial { position: absolute; left: 462px; top: 882px; width: 400px; text-align: center; }
  .testimonial blockquote { font: 600 18px/21px "Cormorant SC", serif; color: var(--navy); letter-spacing: .3px; }
  .testimonial cite { display: block; margin-top: 8px; font: 700 15px/1 "Arimo", sans-serif; font-style: normal; color: var(--ink); }
  .details { position: absolute; left: 462px; top: 971px; width: 400px; }
  .details div { display: flex; margin-bottom: 13px; }
  .details dt { width: 82px; flex: none; text-align: right; padding-right: 13px; font: 700 12px/18px "Roboto Condensed", sans-serif; color: var(--white); }
  .details dd { font: 400 14.5px/17.5px "Jost", sans-serif; color: var(--white); }
  .details .row-who { margin-bottom: 18px; }
  .register { position: absolute; left: 467px; top: 1153px; display: flex; font: 700 14px/17px "Arimo", sans-serif; color: var(--ink); }
  .register-label { font: 700 14px/17px "Roboto Condensed", sans-serif; color: var(--blue); margin-right: 10px; }
  .brand { position: absolute; left: 48px; top: 1082px; display: flex; align-items: center; }
  .brand-mark { width: 44px; height: 44px; border-radius: 50%; background: var(--navy); margin-right: 14px; }
  .brand-name { font: 700 22px/1 "Arimo", sans-serif; color: var(--navy); }
  .brand-rule { position: absolute; left: 90px; top: 1156px; width: 342px; height: 6px;
    background: linear-gradient(180deg, var(--brick) 0 33%, var(--gold) 33% 66%, var(--blue) 66% 100%); }
  .brand-credit { position: absolute; left: 136px; top: 1166px; font: 400 15px/1 "Jost", sans-serif; color: var(--blue); }
  .brand-credit span { color: var(--brick); margin: 0 6px; }
</style>
</head>
<body>
<main class="flyer">
  <svg class="backdrop" width="868" height="1200" viewBox="0 0 868 1200" aria-hidden="true">
    <defs>
      <linearGradient id="header-fill" x1="0" y1="0" x2="1" y2="0">
        <stop offset="0" stop-color="#2258ad"/>
        <stop offset=".55" stop-color="#1a2f86"/>
        <stop offset="1" stop-color="#13105a"/>
      </linearGradient>
      <linearGradient id="footer-fill" x1="0" y1="0" x2="1" y2="0">
        <stop offset="0" stop-color="#2258ad"/>
        <stop offset="1" stop-color="#14115c"/>
      </linearGradient>
    </defs>
    <path d="M868 24 H620 C575 24 565 94 520 94 H0 V415 H400 C450 415 455 342 505 342 H868 Z" fill="url(#header-fill)"/>
    <path d="M0 955 H868 V1134 H475 C425 1134 420 1064 366 1064 H0 Z" fill="url(#footer-fill)"/>
  </svg>

  <h1 class="headline">Organize and Revitalize Your Life.</h1>
  <div class="presenter">
    <p class="presenter-name">Maren Holtby</p>
    <p class="presenter-role">Cognitive Therapist</p>
  </div>

  <div class="brain-art" role="img" aria-label="Illustration of a brain made of colourful interlocking gears"></div>
  <svg class="backdrop" width="868" height="1200" viewBox="0 0 868 1200" aria-hidden="true">
    <g stroke="#f2cf2a" stroke-width="2.5" fill="none">
      <polyline points="198,151 225,176 626,176"/>
      <polyline points="227,245 240,242 520,242"/>
      <polyline points="198,330 225,304 558,304"/>
    </g>
    <g fill="#f2cf2a">
      <path d="M624 164 L638 176 L624 188 Z"/>
      <path d="M518 230 L532 242 L518 254 Z"/>
      <path d="M556 292 L570 304 L556 316 Z"/>
    </g>
    <g fill="#ffffff">
      <circle cx="198" cy="151" r="14"/>
      <circle cx="227" cy="245" r="14"/>
      <circle cx="198" cy="330" r="14"/>
    </g>
  </svg>
  <ul class="steps">
    <li>GOALS</li>
    <li>ACTIVITIES</li>
    <li>ACTIONS</li>
  </ul>

  <ul class="benefits">
    <li>Free your mind, revitalize your life, enjoy relationships more, feel happier and have greater meaning in your life by being organized.</li>
    <li>Spend Three - 3 hour sessions making your life less stressed and creating a realistic picture of what needs to be accomplished.</li>
    <li>Become more effective in everything you do so you have more time for things you value most.</li>
    <li>Walk away with major goals broken down into their component parts and organized on a yearly calendar.</li>
    <li>Complete your tasks in a fast and fun game format.</li>
    <li>Join a group of people dedicated to organizing all areas of life and tap into their support.</li>
    <li>Enjoy improved mental health and financial fitness by uncluttering your life.</li>
  </ul>
  <div class="benefits-pointer"></div>
  <p class="takeaway">You will walk away with<br>detailed plans for 2013</p>

  <div class="group-photo" role="img" aria-label="Photo of a cheerful group of five adults giving thumbs up"></div>
  <figure class="testimonial">
    <blockquote>"My life is less stressful and happier since completing this Workshop."</blockquote>
    <cite>- Owen Pardee</cite>
  </figure>

  <dl class="details">
    <div class="row-who"><dt>WHO:</dt><dd>Adults of any age including high school and college students ready to develop a plan for your life.</dd></div>
    <div><dt>WHERE:</dt><dd>4971 E Pruett Ave., Kennewick, WA 99336</dd></div>
    <div><dt>WHEN:</dt><dd>March 9, 16, 23 of 2013, 9 a.m. to 12 p.m.</dd></div>
    <div><dt>INVESTMENT:</dt><dd>$597</dd></div>
  </dl>

  <div class="register">
    <span class="register-label">Preregister:</span>
    <p>call or text 509-218-3907 or<br>email mcsh48plan@gmail.com by Friday 2/16/13</p>
  </div>

  <div class="brand">
    <span class="brand-mark"></span>
    <span class="brand-name">The Mindcraft Study House</span>
  </div>
  <div class="brand-rule"></div>
  <p class="brand-credit">Maren Holtby<span>|</span>Cognitive Therapist</p>
</main>
</body>
</html>
```